Business card design needed

My business is in Matchmaking. My objective is to find the most compatible partner for my clients....basically I'm in the love and happiness industry bringing two people together for a lasting loving relationship.

I envision the design to be something with 2 people who are in love looking happy or even a silhouette.....I don't really know, I'm open to ideas.....maybe no picture at all, but I want it to be classy :-)

I do have a logo which I will upload. You can also go to my website to give you an idea on the colours and the design if that helps, however the website is not finished yet, it should be up by today or tomorrow. If the website has a heart with swirls on the upper left hand corner, that is the old website, please ignore that one. The one that will be up shortly has a picture frame on the home page with my logo that will be in the file I will upload on this page.

Target Market(s)

There are three categories: Over 45, Asian and Western and same sex, but would be able to afford to hire a matchmaker

Industry/Entity Type

Industry

Contact Information for Business Card

The Tidewell Bureau
Helping You Find The "One"
Maris Pelloway
Matchmaker
0491 572 064
info@tidewellbureau.com.au
www.tidewellbureau.com.au

```html
<!DOCTYPE html>
<html lang="en">
<head>
<meta charset="utf-8">
<title>The Tidewell Bureau — Business Card</title>
<link href="https://fonts.googleapis.com/css2?family=Montserrat:wght@300;400;500&display=swap" rel="stylesheet">
<style>
  :root {
    --backdrop: #8a8a8a;
    --card: #ffffff;
    --mauve: #7b4b60;
    --ink: #3d3d3d;
    --muted: #8c8c8c;
    --texture-tone: #f3f2f2;
    --floral-tone: #f1efef;
  }
  * { margin: 0; padding: 0; box-sizing: border-box; }
  html, body {
    width: 1200px; height: 1012px; overflow: hidden;
    background: var(--backdrop);
    font-family: "Montserrat", sans-serif;
  }
  .stage {
    position: relative; width: 1200px; height: 1012px;
    display: flex; flex-direction: column; align-items: center; justify-content: center; gap: 60px;
  }
  .card {
    position: relative; width: 600px; height: 343px;
    background: var(--card); border-radius: 28px; overflow: hidden;
    box-shadow: 0 10px 24px rgba(0,0,0,0.18);
  }

  /* contact side */
  .floral-texture {
    position: absolute; inset: 0;
    background: linear-gradient(160deg, var(--floral-tone) 0%, var(--floral-tone) 30%, rgba(241,239,239,0.5) 48%, rgba(255,255,255,0) 62%);
  }
  .identity { position: absolute; left: 44px; top: 196px; }
  .identity .name { font-size: 24px; font-weight: 400; color: var(--mauve); letter-spacing: 0.5px; }
  .identity .role { font-size: 15px; font-weight: 300; color: var(--ink); letter-spacing: 5px; margin-top: 2px; }
  .contacts { position: absolute; left: 330px; top: 118px; }
  .contact { margin-bottom: 16px; }
  .contact .label { font-size: 10px; color: var(--muted); letter-spacing: 0.5px; }
  .contact .value { font-size: 13px; color: var(--ink); letter-spacing: 1.6px; margin-top: 2px; }

  /* brand side */
  .uv-texture {
    position: absolute; inset: 0;
    background: linear-gradient(150deg, var(--texture-tone) 0%, var(--card) 50%, var(--texture-tone) 100%);
  }
  .brand {
    position: absolute; inset: 0;
    display: flex; flex-direction: column; align-items: center; justify-content: center;
  }
  .brand .mark { width: 46px; height: 46px; border-radius: 50%; background: var(--mauve); margin-bottom: 18px; }
  .brand .wordmark { font-size: 32px; font-weight: 400; color: var(--ink); letter-spacing: 1px; }
  .brand .tagline { font-size: 13px; font-weight: 400; color: var(--muted); margin-top: 10px; letter-spacing: 0.5px; }
</style>
</head>
<body>
<main class="stage">
  <section class="card card--contact">
    <div class="floral-texture" role="img" aria-label="Faint floral pattern across the upper left of the card"></div>
    <div class="identity">
      <div class="name">Maris Pelloway</div>
      <div class="role">matchmaker</div>
    </div>
    <div class="contacts">
      <div class="contact"><div class="label">phone</div><div class="value">0491 572 064</div></div>
      <div class="contact"><div class="label">web</div><div class="value">www.tidewellbureau.com.au</div></div>
      <div class="contact"><div class="label">mail</div><div class="value">info@tidewellbureau.com.au</div></div>
    </div>
  </section>

  <section class="card card--brand">
    <div class="uv-texture" role="img" aria-label="Diagonal line texture in spot UV across the card"></div>
    <div class="brand">
      <div class="mark"></div>
      <div class="wordmark">The Tidewell Bureau</div>
      <div class="tagline">The Tidewell Bureau Helping You Find The "One"</div>
    </div>
  </section>
</main>
</body>
</html>
```